Masonry and Landscaping Construction company business card

Looking for a business card design for a construction company named Ferrano Construction. It is an italian-american family business that specializes in custom stone work, patios, walkways, driveways, steps, outdoor kitchens, concrete, waterproofing, power wash, landscaping and more. Our colors are mostly red and white with some black. We're looking for a bold design. we also like to incorporate a picture of my family's hometown somewhere in it.
Target Market(s)
Luxury home owners
Industry/Entity Type
Construction
Contact Information for Business Card
Details includes should be bullet points mentioning the services provided. Custom Stone Work, Outdoor Kitchens, Fire Pits, Patios, Walkways, Steps, Concrete, Waterproofing, powerwash and landscaping
Requirements
Must have
- Would like a spot on the card for co-owners names, numbers and email to be listed also looking to add the QR code for an instagram page
Nice to have
- would like something bold, based around the colors red and white with black outlines or details

```html
<!DOCTYPE html>
<html lang="en">
<head>
<meta charset="utf-8">
<title>Ferrano Construction – Business Card</title>
<link href="https://fonts.googleapis.com/css2?family=Montserrat:wght@500;700;800&family=Poppins:wght@400;500;600&display=swap" rel="stylesheet">
<style>
  :root {
    --brand-red: #d62027;
    --brand-red-dark: #b3161c;
    --brand-green: #1fa94b;
    --ink: #141414;
    --paper: #ffffff;
    --backdrop: #3a3a3a;
  }
  html, body {
    margin: 0;
    width: 1200px;
    height: 900px;
    overflow: hidden;
    background: var(--backdrop);
  }
  .sheet {
    position: relative;
    width: 1200px;
    height: 900px;
    display: flex;
    flex-direction: column;
    align-items: center;
    justify-content: center;
    gap: 40px;
  }
  .card {
    width: 680px;
    height: 388px;
    display: block;
    border-radius: 18px;
    box-shadow: 0 10px 30px rgba(0,0,0,.45);
  }
  .brand-name { font-family: "Montserrat", sans-serif; font-weight: 800; fill: var(--ink); }
  .brand-name--light { fill: var(--paper); }
  .person-name { font-family: "Montserrat", sans-serif; font-weight: 800; fill: var(--brand-red); }
  .person-role { font-family: "Poppins", sans-serif; font-weight: 500; fill: var(--ink); }
  .contact-text { font-family: "Poppins", sans-serif; font-weight: 500; fill: var(--ink); }
  .phone-text { font-family: "Montserrat", sans-serif; font-weight: 700; fill: var(--paper); }
  .services-title { font-family: "Poppins", sans-serif; font-weight: 600; fill: var(--paper); }
  .services-item { font-family: "Poppins", sans-serif; font-weight: 400; fill: var(--paper); }
</style>
</head>
<body>
<main class="sheet">

  <!-- Front -->
  <svg class="card card--front" viewBox="0 0 680 388" xmlns="http://www.w3.org/2000/svg">
    <defs>
      <clipPath id="front-shape"><rect width="680" height="388" rx="18"/></clipPath>
      <linearGradient id="hometown-tones" x1="0" y1="0" x2="0" y2="1">
        <stop offset="0" stop-color="#c9d3dc"/>
        <stop offset="0.35" stop-color="#7f9a6a"/>
        <stop offset="0.65" stop-color="#b58a6c"/>
        <stop offset="1" stop-color="#4f7a3a"/>
      </linearGradient>
    </defs>
    <g clip-path="url(#front-shape)">
      <rect class="card-base" width="680" height="388" fill="var(--paper)"/>

      <polygon class="hometown-photo" role="img" aria-label="Photo of the family's Italian hometown: hillside village with bell tower and green mountains"
        points="0,100 235,100 300,165 300,325 0,325" fill="url(#hometown-tones)"/>
      <polyline class="photo-frame" points="0,100 235,100 300,165 300,325" fill="none" stroke="var(--brand-red)" stroke-width="2"/>
      <polygon class="bottom-rule" points="0,325 300,325 680,302 680,306 300,330 0,330" fill="var(--brand-red)"/>

      <!-- Brand name -->
      <rect class="brand-mark" x="360" y="48" width="22" height="22" fill="var(--brand-red)"/>
      <text class="brand-name" x="394" y="68" font-size="28">FERRANO</text>
      <text class="brand-name" x="394" y="100" font-size="22">CONSTRUCTION</text>

      <!-- Person -->
      <text class="person-name" x="640" y="165" font-size="26" text-anchor="end">MARCO BELLINI</text>
      <text class="person-role" x="640" y="188" font-size="15" text-anchor="end">Managing Director</text>

      <!-- Phone band -->
      <polygon class="phone-band" points="380,205 680,205 680,243 360,243" fill="var(--brand-red)"/>
      <text class="phone-text" x="420" y="232" font-size="21">1.800.555.0142</text>
      <polygon class="phone-tab" points="312,228 352,228 370,262 312,262" fill="var(--brand-green)"/>
      <g class="icon-phone" fill="var(--paper)">
        <path d="M326 239 q10 -6 20 0 l-2 4 h-4 l-1 -2 q-3 -1 -6 0 l-1 2 h-4 z"/>
        <rect x="328" y="244" width="16" height="10" rx="2"/>
      </g>

      <!-- Side tabs -->
      <rect class="tab-green" x="622" y="243" width="18" height="38" fill="var(--brand-green)"/>
      <rect class="tab-red" x="640" y="243" width="40" height="38" fill="var(--brand-red)"/>

      <!-- Website -->
      <polygon class="icon-hex" points="330,270 342,277 342,291 330,298 318,291 318,277" fill="var(--brand-red)"/>
      <circle cx="330" cy="284" r="6" fill="none" stroke="var(--paper)" stroke-width="1.6"/>
      <line x1="324" y1="284" x2="336" y2="284" stroke="var(--paper)" stroke-width="1.2"/>
      <text class="contact-text" x="356" y="290" font-size="16">www.ferranobuild.com</text>

      <!-- Email -->
      <polygon class="icon-hex" points="36,344 48,351 48,365 36,372 24,365 24,351" fill="var(--brand-red)"/>
      <rect x="29" y="353" width="14" height="10" fill="var(--paper)"/>
      <polyline points="29,353 36,359 43,353" fill="none" stroke="var(--brand-red)" stroke-width="1.2"/>
      <text class="contact-text" x="60" y="364" font-size="16">sales@ferranobuild.com</text>
    </g>
  </svg>

  <!-- Back -->
  <svg class="card card--back" viewBox="0 0 680 388" xmlns="http://www.w3.org/2000/svg">
    <rect class="card-base" width="680" height="388" rx="18" fill="var(--brand-red)"/>

    <rect class="brand-mark" x="390" y="112" width="24" height="24" fill="var(--paper)"/>
    <text class="brand-name brand-name--light" x="426" y="134" font-size="34">FERRANO</text>
    <text class="brand-name brand-name--light" x="426" y="168" font-size="24">CONSTRUCTION</text>

    <text class="services-title" x="60" y="130" font-size="22">Our Services</text>
    <g class="services-list" font-size="13">
      <g transform="translate(64,152)"><polygon points="0,-8 7,-4 0,0" fill="var(--paper)"/><text class="services-item" x="16" y="0">Custom Stone Work,</text></g>
      <g transform="translate(64,172)"><polygon points="0,-8 7,-4 0,0" fill="var(--paper)"/><text class="services-item" x="16" y="0">Outdoor Kitchens</text></g>
      <g transform="translate(64,192)"><polygon points="0,-8 7,-4 0,0" fill="var(--paper)"/><text class="services-item" x="16" y="0">Fire Pits</text></g>
      <g transform="translate(64,212)"><polygon points="0,-8 7,-4 0,0" fill="var(--paper)"/><text class="services-item" x="16" y="0">Patios</text></g>
      <g transform="translate(64,232)"><polygon points="0,-8 7,-4 0,0" fill="var(--paper)"/><text class="services-item" x="16" y="0">Walkways</text></g>
      <g transform="translate(64,252)"><polygon points="0,-8 7,-4 0,0" fill="var(--paper)"/><text class="services-item" x="16" y="0">Steps</text></g>
      <g transform="translate(64,272)"><polygon points="0,-8 7,-4 0,0" fill="var(--paper)"/><text class="services-item" x="16" y="0">Concrete</text></g>
      <g transform="translate(64,292)"><polygon points="0,-8 7,-4 0,0" fill="var(--paper)"/><text class="services-item" x="16" y="0">WaterProofing</text></g>
      <g transform="translate(64,312)"><polygon points="0,-8 7,-4 0,0" fill="var(--paper)"/><text class="services-item" x="16" y="0">Power wash &amp; Landscaping</text></g>
    </g>
  </svg>

</main>
</body>
</html>
```